Parcels & Petals
Parcels & Petals - Gifts and Occasions
Creative Brief
Bright & Fun-filled
Ritu Malhotra
C-17, Dilkusha Marg Lucknow - 226014
ritumal47@postbright.example
www.parcelspetals.example
I want the logo on one side and the other details on the other side. The logo to be used is draft no. 3 in my project parcels and petals

```html
<!DOCTYPE html>
<html lang="en">
<head>
<meta charset="utf-8">
<title>Parcels &amp; Petals – Business Card</title>
<link href="https://fonts.googleapis.com/css2?family=Varela+Round&display=swap" rel="stylesheet">
<style>
  :root{
    --bg:#e9e9ea;
    --card:#ffffff;
    --blue:#2f9fd8;
    --green:#7cc242;
    --orange:#f4a41d;
    --red:#ee4036;
    --pink:#ec4f91;
    --silver:#c9ced3;
    --ink:#4a4a4a;
    --muted:#7a7a7a;
  }
  *{margin:0;padding:0;box-sizing:border-box}
  html,body{width:1200px;height:838px;overflow:hidden}
  body{
    background:var(--bg);
    font-family:"Varela Round",Arial,sans-serif;
    display:flex;align-items:center;justify-content:center;
  }
  .card{
    position:relative;width:1000px;height:572px;background:var(--card);
    border-radius:14px;overflow:hidden;
    box-shadow:0 10px 30px rgba(0,0,0,.12);
  }
  .brand{
    position:absolute;left:70px;top:150px;width:440px;
    display:flex;align-items:center;gap:16px;
  }
  .brand-dot{width:22px;height:22px;background:var(--blue);border-radius:4px;flex:none}
  .brand-name{font-size:46px;color:var(--blue);letter-spacing:.5px;line-height:1.1}
  .details{
    position:absolute;left:560px;top:170px;padding-left:26px;
    border-left:4px solid transparent;
  }
  .divider{position:absolute;left:560px;top:170px;width:4px;height:150px}
  .person{font-size:34px;color:var(--blue)}
  .role{font-size:17px;color:var(--muted);margin:4px 0 22px}
  .address{font-size:20px;color:var(--ink);line-height:1.35;margin-bottom:18px}
  .contact{display:flex;align-items:center;gap:10px;font-size:20px;color:var(--ink);margin-bottom:8px}
  .contact svg{flex:none}
  .website{
    position:absolute;left:150px;bottom:44px;
    font-size:24px;letter-spacing:8px;color:var(--muted);
  }
  .band{position:absolute;left:0;right:0;bottom:0;height:30px;display:flex}
  .band span{display:block;height:100%}
  .b-blue{background:var(--blue);width:13%}
  .b-green{background:var(--green);width:38%}
  .b-orange{background:var(--orange);width:17%}
  .b-red{background:var(--red);width:10%}
  .b-pink{background:var(--pink);width:15%}
  .b-silver{background:var(--silver);width:7%}
</style>
</head>
<body>
  <div class="card">
    <div class="brand">
      <span class="brand-dot"></span>
      <span class="brand-name">Parcels &amp; Petals</span>
    </div>

    <svg class="divider" viewBox="0 0 4 150" preserveAspectRatio="none" aria-hidden="true">
      <rect x="0" y="0" width="4" height="30" fill="#2f9fd8"/>
      <rect x="0" y="30" width="4" height="30" fill="#7cc242"/>
      <rect x="0" y="60" width="4" height="30" fill="#f4a41d"/>
      <rect x="0" y="90" width="4" height="30" fill="#ee4036"/>
      <rect x="0" y="120" width="4" height="30" fill="#ec4f91"/>
    </svg>

    <div class="details">
      <div class="person">Ritu Malhotra</div>
      <div class="role">President / CEO</div>
      <div class="address">C-17, Dilkusha Marg<br>Lucknow - 226014</div>
      <div class="contact">
        <svg width="20" height="20" viewBox="0 0 20 20" aria-hidden="true">
          <rect x="5" y="1" width="10" height="18" rx="2" fill="#f4a41d"/>
          <rect x="7" y="4" width="6" height="10" fill="#fff"/>
        </svg>
        <span>: 9415207316</span>
      </div>
      <div class="contact">
        <svg width="20" height="20" viewBox="0 0 20 20" aria-hidden="true">
          <rect x="1" y="4" width="18" height="12" rx="2" fill="#ee4036"/>
          <path d="M2 5 L10 11 L18 5" stroke="#fff" stroke-width="1.6" fill="none"/>
        </svg>
        <span>: ritumal47@postbright.example</span>
      </div>
    </div>

    <div class="website">www.parcelspetals.example</div>

    <div class="band">
      <span class="b-blue"></span><span class="b-green"></span><span class="b-orange"></span>
      <span class="b-red"></span><span class="b-pink"></span><span class="b-silver"></span>
    </div>
  </div>
</body>
</html>
```